The Northmoor Aid League needs a graphic of their innovation approach

What we need?
- we have designed a new innovation approach (see attached). An innovation approach is the process one goes through in order to design and launch a new product or service.
- This new graphic will be used in meetings to help others understand what innovation is and how we do it. It will also be used in training sessions and be the starting point for innovation training materials we are creating
- We have created this draft graphic by copying and pasting new words over another charities innovation process
- We would like you to use your design magic and create our very own innovation process graphic. We would like it to be neat, simple, non fussy, easy to understand /read and in line with our brand colours
Attached:
1. PowerPoint:
- Slide 1: our innovation process
- Slide 2 explanation of process to bring it to life
- Slide 3&4: brand colours
- Slide 5: inspiration / examples of other processes we like the look of
2. Typeface brand guidelines
We can't wait to see what you come up with! Thank you :)
internal employees
Charity

```html
<!DOCTYPE html>
<html lang="en">
<head>
<meta charset="utf-8">
<title>Innovation Approach – The Northmoor Aid League</title>
<link href="https://fonts.googleapis.com/css2?family=Roboto:wght@400;500&display=swap" rel="stylesheet">
<style>
  :root {
    --bg-top: #f0eff0;
    --bg-bottom: #dcdadd;
    --card: #f6f6f7;
    --disc: #eceaec;
    --ink: #1d1d1f;
    --red: #ff0a3c;
    --red-deep: #e51d2a;
    --purple: #9a1ee0;
    --purple-light: #b443f2;
    --blue: #0a72e6;
    --blue-deep: #2a4fd2;
    --cyan: #15c4e2;
    --cyan-light: #18e4f2;
    --orange: #ff8c00;
    --orange-light: #ffb400;
    --white: #ffffff;
  }
  html, body { margin: 0; padding: 0; overflow: hidden; }
  body { width: 1200px; height: 1200px; }
  .canvas { display: block; width: 1200px; height: 1200px; font-family: "Roboto", Arial, sans-serif; }
  .card { fill: var(--card); }
  .ring-disc { fill: var(--disc); }
  .heading { font-size: 31px; font-weight: 500; fill: var(--ink); }
  .heading--red { fill: var(--red); }
  .body-small { font-size: 13px; fill: var(--ink); }
  .body-large { font-size: 18px; fill: var(--ink); }
  .tab-label { font-size: 26px; font-weight: 500; fill: var(--white); }
  .tab-label--spaced { letter-spacing: 3px; }
  .tab-label--dark { fill: var(--ink); }
  .tab-label--small { font-size: 21px; }
  .icon { fill: var(--white); }
</style>
</head>
<body>
<svg class="canvas" viewBox="0 0 1600 1600" xmlns="http://www.w3.org/2000/svg">
  <defs>
    <linearGradient id="bg" x1="0" y1="0" x2="1" y2="1">
      <stop offset="0" stop-color="var(--bg-top)"/><stop offset="1" stop-color="var(--bg-bottom)"/>
    </linearGradient>
    <linearGradient id="g-red" x1="0" y1="0" x2="1" y2="0"><stop offset="0" stop-color="var(--red-deep)"/><stop offset="1" stop-color="var(--red)"/></linearGradient>
    <linearGradient id="g-purple" x1="1" y1="0" x2="0" y2="0"><stop offset="0" stop-color="var(--purple)"/><stop offset="1" stop-color="var(--purple-light)"/></linearGradient>
    <linearGradient id="g-blue" x1="0" y1="0" x2="1" y2="0"><stop offset="0" stop-color="var(--blue-deep)"/><stop offset="1" stop-color="var(--blue)"/></linearGradient>
    <linearGradient id="g-cyan" x1="1" y1="0" x2="0" y2="0"><stop offset="0" stop-color="var(--cyan-light)"/><stop offset="1" stop-color="var(--cyan)"/></linearGradient>
    <linearGradient id="g-orange" x1="0" y1="0" x2="1" y2="0"><stop offset="0" stop-color="var(--orange)"/><stop offset="1" stop-color="var(--orange-light)"/></linearGradient>
    <filter id="soft-shadow" x="-30%" y="-30%" width="160%" height="160%">
      <feDropShadow dx="0" dy="6" stdDeviation="10" flood-color="#000" flood-opacity="0.18"/>
    </filter>
  </defs>

  <rect width="1600" height="1600" fill="url(#bg)"/>

  <!-- content cards -->
  <rect class="card" x="178" y="237" width="640" height="225" rx="24"/>
  <rect class="card" x="790" y="475" width="636" height="225" rx="24"/>
  <rect class="card" x="178" y="712" width="640" height="225" rx="24"/>
  <rect class="card" x="790" y="951" width="636" height="225" rx="24"/>
  <rect class="card" x="178" y="1188" width="640" height="225" rx="24"/>

  <!-- outer discs -->
  <g class="outer-discs" filter="url(#soft-shadow)">
    <circle class="ring-disc" cx="802" cy="350" r="168"/>
    <circle class="ring-disc" cx="802" cy="587" r="168"/>
    <circle class="ring-disc" cx="802" cy="825" r="168"/>
    <circle class="ring-disc" cx="802" cy="1062" r="168"/>
    <circle class="ring-disc" cx="802" cy="1300" r="168"/>
  </g>

  <!-- step ribbons -->
  <g class="ribbon ribbon--challenge" fill="url(#g-red)">
    <path d="M802,225 A125,125 0 0 1 802,475 Z"/>
    <path d="M870,250 C900,275 920,283 960,283 L1098,283 L1132,350 L1098,417 L960,417 C920,417 900,425 870,450 Z"/>
  </g>
  <g class="ribbon ribbon--opportunity" fill="url(#g-purple)">
    <path d="M802,462 A125,125 0 0 0 802,712 Z"/>
    <path d="M734,487 C704,512 684,520 644,520 L506,520 L472,587 L506,654 L644,654 C684,654 704,662 734,687 Z"/>
  </g>
  <g class="ribbon ribbon--concepts" fill="url(#g-blue)">
    <path d="M802,700 A125,125 0 0 1 802,950 Z"/>
    <path d="M870,725 C900,750 920,758 960,758 L1098,758 L1132,825 L1098,892 L960,892 C920,892 900,900 870,925 Z"/>
  </g>
  <g class="ribbon ribbon--solution" fill="url(#g-cyan)">
    <path d="M802,937 A125,125 0 0 0 802,1187 Z"/>
    <path d="M734,962 C704,987 684,995 644,995 L506,995 L472,1062 L506,1129 L644,1129 C684,1129 704,1137 734,1162 Z"/>
  </g>
  <g class="ribbon ribbon--launch" fill="url(#g-orange)">
    <path d="M802,1175 A125,125 0 0 1 802,1425 Z"/>
    <path d="M870,1200 C900,1225 920,1233 960,1233 L1098,1233 L1132,1300 L1098,1367 L960,1367 C920,1367 900,1375 870,1400 Z"/>
  </g>

  <!-- inner discs -->
  <g class="inner-discs" filter="url(#soft-shadow)">
    <circle class="ring-disc" cx="802" cy="350" r="112"/>
    <circle class="ring-disc" cx="802" cy="587" r="112"/>
    <circle class="ring-disc" cx="802" cy="825" r="112"/>
    <circle class="ring-disc" cx="802" cy="1062" r="112"/>
    <circle class="ring-disc" cx="802" cy="1300" r="112"/>
  </g>

  <!-- icon badges -->
  <g class="badge" filter="url(#soft-shadow)">
    <circle cx="802" cy="350" r="85" fill="var(--red-deep)"/>
    <circle cx="802" cy="350" r="66" fill="var(--red)"/>
    <circle cx="802" cy="587" r="85" fill="var(--purple)"/>
    <circle cx="802" cy="587" r="66" fill="var(--purple-light)"/>
    <circle cx="802" cy="825" r="85" fill="var(--blue-deep)"/>
    <circle cx="802" cy="825" r="66" fill="var(--blue)"/>
    <circle cx="802" cy="1062" r="85" fill="var(--cyan)"/>
    <circle cx="802" cy="1062" r="66" fill="var(--cyan-light)"/>
    <circle cx="802" cy="1300" r="85" fill="var(--orange)"/>
    <circle cx="802" cy="1300" r="66" fill="var(--orange-light)"/>
  </g>

  <!-- icons -->
  <g class="icon icon--home">
    <path d="M800,312 L758,345 L758,354 L800,322 L842,354 L842,345 Z"/>
    <path d="M770,352 L800,330 L830,352 L830,386 L810,386 L810,372 A10,10 0 0 0 790,372 L790,386 L770,386 Z"/>
  </g>
  <g class="icon icon--bulb">
    <path d="M800,553 A27,27 0 0 0 785,603 L787,612 L813,612 L815,603 A27,27 0 0 0 800,553 Z"/>
    <rect x="787" y="615" width="26" height="5" rx="2"/>
    <rect x="790" y="623" width="20" height="5" rx="2"/>
    <path d="M786,580 A14,14 0 0 1 796,566" fill="none" stroke="var(--purple-light)" stroke-width="4" stroke-linecap="round"/>
  </g>
  <g class="icon icon--chat">
    <path d="M800,788 A36,33 0 1 1 788,852 L776,862 L779,848 A36,33 0 0 1 800,788 Z"/>
    <circle cx="787" cy="822" r="3.5" fill="var(--blue)"/>
    <circle cx="800" cy="822" r="3.5" fill="var(--blue)"/>
    <circle cx="813" cy="822" r="3.5" fill="var(--blue)"/>
  </g>
  <g class="icon icon--gear">
    <g transform="translate(800,1062)">
      <rect x="-8" y="-39" width="16" height="78" rx="2"/>
      <rect x="-8" y="-39" width="16" height="78" rx="2" transform="rotate(45)"/>
      <rect x="-8" y="-39" width="16" height="78" rx="2" transform="rotate(90)"/>
      <rect x="-8" y="-39" width="16" height="78" rx="2" transform="rotate(135)"/>
      <circle r="29"/>
      <circle r="11" fill="var(--cyan-light)"/>
    </g>
  </g>
  <g class="icon icon--briefcase">
    <path d="M782,1272 L818,1272 L818,1284 L812,1284 L812,1278 L788,1278 L788,1284 L782,1284 Z"/>
    <rect x="764" y="1284" width="72" height="46" rx="2"/>
    <rect x="764" y="1297" width="72" height="3" fill="var(--orange-light)"/>
  </g>

  <!-- tab labels -->
  <text class="tab-label" x="938" y="359">CHALLENGE</text>
  <text class="tab-label tab-label--small" x="513" y="583">OPPORTUNITY</text>
  <text class="tab-label tab-label--small" x="513" y="609">STATEMENT</text>
  <text class="tab-label tab-label--spaced" x="936" y="834">CONCEPTS</text>
  <text class="tab-label tab-label--spaced" x="516" y="1070">SOLUTION</text>
  <text class="tab-label tab-label--spaced tab-label--dark" x="942" y="1310">LAUNCH</text>

  <!-- step descriptions -->
  <g class="step step--insight" text-anchor="end">
    <text class="heading heading--red" x="512" y="302">INSIGHT</text>
    <text class="body-small" x="581" y="332">at the beginning of the project you need to define your</text>
    <text class="body-small" x="581" y="348">challenge (i.e. How might we ................. (what you want to</text>
    <text class="body-small" x="581" y="364">accomplish), for ........................ (to whom your impact will</text>
    <text class="body-small" x="581" y="380">matter most to), in a way that .................. (describe the</text>
    <text class="body-small" x="581" y="396">approach, mindset, or values you want to apply), so that</text>
    <text class="body-small" x="581" y="412">.................... (the big impact you want to create).</text>
  </g>
  <g class="step step--ideate">
    <text class="heading heading--red" x="1001" y="528">IDEATE</text>
    <text class="body-small" x="1001" y="561">now you will be able to articulate a prioritised problem or list</text>
    <text class="body-small" x="1001" y="580">of problems you want to solve (we like to phrase them in a</text>
    <text class="body-small" x="1001" y="598">more positive way – hence the use of the word</text>
    <text class="body-small" x="1001" y="617">‘opportunities’ rather than ‘problems’)   Without a clear</text>
    <text class="body-small" x="1001" y="636">opportunity statement, it’s time to pivot back to redefining</text>
    <text class="body-small" x="1001" y="655">your problem</text>
  </g>
  <g class="step step--invalidate">
    <text class="heading" x="606" y="764" text-anchor="end">(IN)VALIDATE</text>
    <text class="body-large" x="229" y="801">1-3 ‘concepts’ to test (i.e. prototype/pilot)</text>
  </g>
  <g class="step step--test">
    <text class="heading" x="1001" y="1020">TEST</text>
    <text class="body-large" x="1001" y="1058">Lorem ipsum dolor sit amet, consectetuer</text>
    <text class="body-large" x="1001" y="1079">adipiscing elit, sed diam nonummy nibh</text>
    <text class="body-large" x="1001" y="1100">euismod tincidunt ut laoreet</text>
  </g>
  <g class="step step--delivery" text-anchor="end">
    <text class="heading" x="584" y="1251">DELIVERY</text>
    <text class="heading" x="584" y="1288">PLAN</text>
    <text class="body-large" x="584" y="1321">Lorem ipsum dolor sit amet, consectetuer</text>
    <text class="body-large" x="584" y="1342">adipiscing elit, sed diam nonummy nibh</text>
    <text class="body-large" x="584" y="1363">euismod tincidunt ut laoreet</text>
  </g>
</svg>
</body>
</html>
```